Re-design of our website - Property Development Company

Our current website is now old and stale. We are looking for a Wordpress design for a new website. Our company is a property development and property investment company. We have different projects that are under construction and have completed a number also. We would like to showcase these projects as individual pages. The projects are located all over the east coast of Australia and a mixture of retail, industrial, residential subdivsions. In the near future we are hoping to start a small property funds management division as well.

Current website is www.korvanith.com.au

We are wanting you to design a page for the each of following (total of 3 pages):
- Home page
- Project page (which will be used to showcase each development project). There are 4 active projects that we currently own and a number of completed projects.
- Information page (which will be used for about us, contact us, management etc.)

Feel free to go out of the box and wow us. We are open to new ideas.
Updates

Reason: Hi I am going on annual leave for a week being 17-21 Feb so wont be able to comment on anyones design so I have given you an extra week and a bit to finish off your 3 pages. Thanks for the designs so far, they are looking good.

Target Market(s)

It will be used by business professionals researching our company including:
- current investors
- new investors
- consultants (architects, builders, town planners, council, real estate managers/agents, engineers etc.)
- Bank lenders

We want these people to think yes we want to work with this company, they look like they are exceptional at what they do, professional, highly capable.

Industry/Entity Type

Investment

Requirements
Must have
• Our Logo. Files attached. This can be modified if you think it needs to be improved.
Nice to have
• We like clean looking websites.
• We will have some professional photographs taken of our current property developments once they are completed - two shopping centres that will be our signature developments to date. For the time being I have uploaded some aerial photographs on one of our projects under construction and also some nice photos of one of our completed developments. This should help with designing the project page.
Should not have
• We don't like busy websites with too much going on and you don't know what to look at.

```html
<!DOCTYPE html>
<html lang="en">
<head>
<meta charset="utf-8">
<title>Korvanith Partners – Philosophy</title>
<link rel="stylesheet" href="https://fonts.googleapis.com/css2?family=Share+Tech+Mono&family=Open+Sans:wght@300;400&display=swap">
<style>
  :root {
    --brand-blue: #0a84ff;
    --deep-blue: #0d4f8a;
    --heading-blue: #14507f;
    --nav-grey: #4a4a4a;
    --body-grey: #444;
    --page-bg: #f1f1f1;
    --panel-bg: #ffffff;
    --rule: #1f5f98;
  }
  * { box-sizing: border-box; margin: 0; padding: 0; }
  html, body { width: 1200px; height: 938px; overflow: hidden; }
  body {
    background: var(--page-bg);
    border-top: 3px solid var(--brand-blue);
    font-family: "Open Sans", sans-serif;
    font-weight: 300;
    color: var(--body-grey);
  }
  .site { position: relative; width: 900px; margin: 0 auto; height: 935px; }
  .site-header { position: relative; height: 173px; }
  .partner-login {
    position: absolute; left: 1px; top: 0; width: 134px; height: 37px;
    background: var(--brand-blue); color: #fff;
    font-family: "Share Tech Mono", monospace; font-size: 13px; letter-spacing: 1.5px;
    display: flex; align-items: center; justify-content: center; text-decoration: none;
  }
  .tagline {
    position: absolute; left: 21px; top: 86px;
    font-family: "Share Tech Mono", monospace; font-weight: 400;
    font-size: 30px; line-height: 36px; letter-spacing: 3px; color: var(--deep-blue);
    white-space: nowrap;
  }
  .main-nav a {
    position: absolute; top: 141px;
    font-family: "Share Tech Mono", monospace; font-size: 15px; letter-spacing: 1.1px;
    line-height: 18px; white-space: nowrap;
    color: var(--nav-grey); text-decoration: none;
  }
  .main-nav a.is-active { color: var(--brand-blue); }
  .brand {
    position: absolute; right: 12px; top: 100px;
    font-family: "Open Sans", sans-serif; font-weight: 400; font-size: 24px;
    line-height: 27px; color: #222; display: flex; align-items: center; gap: 10px;
  }
  .brand-name { text-align: right; }
  .brand-square { width: 14px; height: 14px; background: var(--brand-blue); }
  .header-bar { position: absolute; left: 0; bottom: 0; width: 100%; height: 5px; background: #0a6fd0; }
  .content {
    background: var(--panel-bg);
    box-shadow: 0 0 24px rgba(0,0,0,0.08);
    padding: 30px 45px 0 41px;
    height: 762px; overflow: hidden;
  }
  .page-title {
    font-family: "Share Tech Mono", monospace; font-weight: 400;
    font-size: 20px; letter-spacing: 1.6px; color: var(--heading-blue);
    margin-left: 3px;
  }
  .section-title {
    font-family: "Share Tech Mono", monospace; font-weight: 400;
    font-size: 15px; letter-spacing: 1.5px; color: var(--heading-blue);
    margin: 42px 0 13px;
  }
  .content p { font-size: 13px; line-height: 22.5px; margin-bottom: 5.5px; }
  .rule { border: 0; border-top: 1px solid var(--rule); margin: 22px 0 0; }
  .opportunities { list-style: none; margin-bottom: 5.5px; }
  .opportunities li { font-size: 13px; line-height: 22.5px; padding-left: 14px; position: relative; }
  .opportunities li::before {
    content: ""; position: absolute; left: 0; top: 9px; width: 6px; height: 6px; background: #555;
  }
  .section-focus .section-title { margin-top: 28px; margin-bottom: 15px; }
  .section-philosophy .section-title { margin-top: 30px; }
</style>
</head>
<body>
<div class="site">
  <header class="site-header">
    <a class="partner-login" href="#">PARTNER LOGIN</a>
    <h1 class="tagline">SUCCESS THROUGH DICIPLINE</h1>
    <nav class="main-nav">
      <a href="#" style="left:22px">HOME</a>
      <a href="#" style="left:84px">PHILOSOPHY</a>
      <a href="#" class="is-active" style="left:196px">-ACTIVITIES &amp; PROJECTS</a>
      <a href="#" style="left:416px">MANAGEMENTS</a>
      <a href="#" style="left:541px">FILE UPLOAD</a>
    </nav>
    <div class="brand"><span class="brand-square"></span><span class="brand-name">Korvanith<br>Partners</span></div>
    <div class="header-bar"></div>
  </header>

  <main class="content">
    <h2 class="page-title">PHILOSOPHY</h2>

    <section class="section-difference">
      <h3 class="section-title">THE KORVANITH DIFFERENCE</h3>
      <p>Korvanith Partners brings the best of both the institutional and private worlds to every transaction it is involved in. Having capital resources comparable to many institutions, coupled with the creativity, speed and flexibility of a well established and very private boutique gives us a noticeable point of difference over our competitors.</p>
      <p>As a fiercely private group, we provide our partners and vendors with utmost confidentiality and flexibility in transaction structuring. We pride ourselves on our ability to creatively structure transactions in a way that enables us to proceed with projects when others may not.</p>
      <p>Being averse to high levels of debt, we always contribute a significant equity component to every project which gives us the flexibility to respond quickly to changing financial environments. All of our equity is “in house” and as such, our transactions do not require any external capital raising.</p>
      <hr class="rule">
    </section>

    <section class="section-focus">
      <h3 class="section-title">FOCUS</h3>
      <p>Korvanith is fortunate not to have the restrictions of pre-defined investment guidelines or capital allocation requirements that often limit other investors. This flexibility allows Korvanith to pursue projects for the right reasons rather than ones that merely satisfy an investment committee’s check list.</p>
      <p>We actively seek value add projects of $5m to $40m in size that can be realised in a 1–3 year investment horizon and can encompass opportunities such as:</p>
      <ul class="opportunities">
        <li>traditional development of substantially vacant sites;</li>
        <li>strata and land subdivisions;</li>
        <li>refurbishments and re-leasing;</li>
        <li>trading opportunities; and</li>
        <li>any combination of the above</li>
      </ul>
      <p>Our location selections are also quite diverse, having successfully acquired and delivered projects in metropolitan and regional areas of the east coast of Australia, from Queensland to Tasmania.</p>
      <hr class="rule" style="margin-top:33px">
    </section>

    <section class="section-philosophy">
      <h3 class="section-title">PHILOSOPHY</h3>
    </section>
  </main>
</div>
</body>
</html>
```